Luxury Home Builder looking for an Exciting Email Marketing Campaign

We need to attract real estate agents and brokers to bring us clients and get the maximum possible commission of 10% for bringing us a client to design-build a custom home. We will be sending an email to the top producers offering a 10% commission for a broker bringing us a client to build in Miami Beach. Our homes are beautiful and varied,and we want an attractive email. Please use website for photos and text, winner will be granted full digital files to finalize the work. harborlinecrestbuilds.example

Target Market(s)

Luxury real estate agents and brokers

Industry/Entity Type

Real Estate Development

Requirements
Must have
• Photography of our properties from harborlinecrestbuilds.example
• Design-Build is what we do, saving homebuyers significant money in the process, while building their dream custom homes.
• How would you like to get paid a 10% commission for bringing us a client to build their dream home in Miami Beach, Heron Shoals, and Key Biscayne.
• We are a one-stop boutique construction company that has completed over 300,000 square feet of luxury residences in some of the most prestigious addresses in Dade County. We take our clients by the hand and guide them through the entire process of the home construction, from start to finish.

```html
<!DOCTYPE html>
<html lang="en">
<head>
<meta charset="utf-8">
<title>Harborline Crest – Broker Commission Offer</title>
<link href="https://fonts.googleapis.com/css2?family=Roboto:wght@400;500;700&display=swap" rel="stylesheet">
<style>
:root{
  --navy:#2e4a72;
  --navy-dark:#2c4466;
  --blue:#4c7fc2;
  --blue-section:#5a8ed2;
  --red:#a83a3a;
  --social-red:#c0353a;
  --gold:#c98a2e;
  --gold-light:#e0a84a;
  --text:#3a3a3a;
  --muted:#555;
  --panel:#f6f6f6;
  --line:#dedede;
}
*{box-sizing:border-box;margin:0;padding:0}
html,body{width:1200px;height:2739px;overflow:hidden;background:#fff}
body{font-family:"Roboto",Arial,sans-serif;color:var(--text);position:relative}
.abs{position:absolute}
.preheader{left:200px;top:17px;font-size:11px;color:#555}
.preheader a{color:#1a3aa0;font-weight:500}
.email{left:197px;top:48px;width:814px;height:2600px}
.frame{left:0;top:0;width:814px;height:1776px;border:1px solid #cfcfcf;border-top:3px solid var(--navy)}
.header{left:0;top:0;width:814px;height:137px;background:#fff}
.brand{left:60px;top:24px;width:160px;text-align:center}
.brand-mark{display:block;margin:0 auto 8px;width:40px;height:40px;border-radius:50%;background:var(--gold)}
.brand-name{font-size:19px;font-weight:500;letter-spacing:2px;color:var(--navy-dark);line-height:1.15}
.follow{left:545px;top:32px;width:210px;text-align:center}
.follow-title{font-size:17px;font-weight:500;color:#8b2a2e;margin-bottom:10px}
.socials{display:flex;gap:5px;justify-content:center}
.socials span{width:36px;height:36px;border-radius:50%;background:var(--social-red);display:block}
.hero{left:0;top:137px;width:814px;height:367px;background:linear-gradient(180deg,#1d2a8c 0%,#2d3a9a 28%,#8c93a8 45%,#d7cbb0 62%,#5fa4bd 82%,#2e7fa6 100%)}
.offer{left:0;top:504px;width:814px;height:96px;background:linear-gradient(180deg,var(--gold-light),var(--gold) 60%,#b87a26);color:#fff;text-align:center;text-shadow:0 1px 2px rgba(0,0,0,.35)}
.offer p{font-size:22px;line-height:1.3;padding-top:12px}
.offer strong{font-size:36px;font-weight:700;margin-right:10px}
.shadow{left:60px;width:694px;height:24px;background:radial-gradient(ellipse at top,rgba(0,0,0,.3),rgba(0,0,0,0) 70%)}
.intro-title{left:0;top:648px;width:814px;text-align:center;font-size:30px;font-weight:500;color:var(--navy)}
.intro-copy{left:24px;top:711px;width:776px;font-size:15px;line-height:19.5px;color:var(--muted)}
.btn{left:314px;top:861px;width:213px;height:55px;background:var(--red);color:#fff;font-weight:500;font-size:18px;text-align:center;line-height:55px}
.difference{left:1px;top:964px;width:812px;height:811px;background:var(--panel)}
.section-title{width:100%;text-align:center;font-size:35px;font-weight:500}
.difference .section-title{top:48px;color:var(--navy)}
.divider-v{left:603px;top:1122px;width:1px;height:625px;background:var(--line)}
.divider-h{left:219px;top:1462px;width:763px;height:1px;background:var(--line)}
.feature .icon{width:106px;height:106px}
.feature h3{font-size:18px;font-weight:400;color:var(--navy);line-height:22px;margin-bottom:14px;text-transform:uppercase}
.feature p{font-size:13.6px;line-height:18px;color:var(--muted)}
.feature-body{width:218px}
.portfolio{left:197px;top:1822px;width:814px;height:666px;background:var(--blue-section)}
.portfolio .section-title{top:30px;color:#fff}
.card{width:377px;height:238px;overflow:hidden;box-shadow:0 10px 12px -6px rgba(0,0,0,.35)}
.card .photo{width:100%;height:100%}
.card .caption{left:0;bottom:0;width:100%;height:60px;background:rgba(235,240,230,.85);color:var(--navy);font-size:17px;font-weight:500;padding:22px 14px 0}
.p1{background:linear-gradient(180deg,#f4f6f2 0%,#4f6e3c 40%,#b67a5a 65%,#3a5a2b 100%)}
.p2{background:linear-gradient(180deg,#3d7fd9 0%,#9fc6ef 35%,#31622d 60%,#e6e1d4 80%)}
.p3{background:linear-gradient(180deg,#6b9cde 0%,#dfe8f3 35%,#b7a48b 65%,#5d7a3b 100%)}
.p4{background:linear-gradient(180deg,#3f6e2c 0%,#b9614a 50%,#6d3f2c 75%,#2f4f24 100%)}
.footer{left:197px;top:2488px;width:814px;height:158px;background:var(--navy-dark);color:#fff}
.contact{font-size:15px;line-height:24px}
.contact svg{position:absolute;left:0;top:2px}
.footer-split{left:448px;top:32px;width:1px;height:96px;background:#7d93b3}
.footer .follow-title{color:#fff;font-size:16px}
.footer .socials span{width:32px;height:32px;background:#fff}
.unsub{left:0;top:2695px;width:1200px;text-align:center;font-size:14px;font-weight:500;color:var(--navy)}
.unsub a{color:inherit}
</style>
</head>
<body>

<p class="abs preheader">Having trouble viewing this email? <a href="#">View in a browser window</a></p>

<div class="abs email">
  <div class="abs frame"></div>

  <header class="abs header">
    <div class="abs brand">
      <span class="brand-mark"></span>
      <div class="brand-name">HARBORLINE<br>CREST</div>
    </div>
    <div class="abs follow">
      <div class="follow-title">Follow Us</div>
      <div class="socials" aria-label="Social links">
        <span></span><span></span><span></span><span></span><span></span>
      </div>
    </div>
  </header>

  <div class="abs hero" role="img" aria-label="Luxury home at dusk with lit interior and pool in front"></div>

  <div class="abs offer">
    <p><strong>GET PAID a 10%</strong>commission for bringing us a client to build<br>their dream home in Miami Beach, Heron Shoals, and Key Biscayne.</p>
  </div>
  <div class="abs shadow" style="top:600px"></div>

  <h1 class="abs intro-title">How Would you Like to Get Paid a 10% Commission</h1>
  <p class="abs intro-copy">Lorem ipsum dolor sit amet, consectetuer adipiscing elit, sed diam nonummy nibh euismod tincidunt ut laoreet dolore magna aliquam erat volutpat. Ut wisi enim ad minim veniam, quis nostrud exerci tation ullamcorper suscipit lobortis nisl ut aliquip ex ea commodo consequat. Duis autem vel eum iriure dolor in hendrerit in vulputate velit esse molestie consequat, vel illum dolore eu feugiat nulla facilisis at vero eros et accumsan et iusto odio dignissim qui blandit praesent luptatum zzril delenit augue duis dolore te feugait nulla facilisi.</p>
  <a class="abs btn" href="#">READ MORE</a>

  <section class="abs difference">
    <h2 class="abs section-title">THE HARBORLINE DIFFERENCE</h2>
  </section>
</div>

<div class="abs divider-v"></div>
<div class="abs divider-h"></div>

<!-- Honesty -->
<div class="abs feature" style="left:218px;top:1151px">
  <svg class="icon" viewBox="0 0 106 106"><rect x="23" y="23" width="60" height="60" transform="rotate(45 53 53)" fill="#4c7fc2"/>
    <g fill="#fff"><circle cx="53" cy="45" r="5"/><rect x="46" y="51" width="14" height="7" rx="3"/><circle cx="40" cy="55" r="4"/><circle cx="66" cy="55" r="4"/><rect x="34" y="60" width="12" height="6" rx="3"/><rect x="60" y="60" width="12" height="6" rx="3"/></g></svg>
</div>
<div class="abs feature feature-body" style="left:352px;top:1147px">
  <h3>Honesty and<br>Transparency</h3>
  <p>Relationships are built on honesty and transparency. At Harborline Crest, when you build a home with us, you are not just buying a structure, but an ongoing relationship. We strive to leave our clients with a sense of trust, honesty and integrity. For this reason, our accounting is always open and transparent, and all purchasing is made through and approved by our clients.</p>
</div>

<!-- Reputation -->
<div class="abs feature" style="left:624px;top:1151px">
  <svg class="icon" viewBox="0 0 106 106"><rect x="23" y="23" width="60" height="60" transform="rotate(45 53 53)" fill="#4c7fc2"/>
    <g fill="#fff"><path d="M44 36h7l4 12h-7zM62 36h-7l-4 12h7z"/><circle cx="53" cy="58" r="10"/></g><circle cx="53" cy="58" r="5" fill="#4c7fc2"/></svg>
</div>
<div class="abs feature feature-body" style="left:757px;top:1150px">
  <h3>Reputation and<br>Track-Record</h3>
  <p>Our homebuyers are the best measure of how well we deliver on our promises. We urge anyone interested in the prospect of working with us, to talk to those who have relied on us in the past to create their homes. We are quick to show you our past projects. Take the time to explore our website, we have published portfolios of the homes we have completed.</p>
</div>

<!-- In-house -->
<div class="abs feature" style="left:218px;top:1488px">
  <svg class="icon" viewBox="0 0 106 106"><rect x="23" y="23" width="60" height="60" transform="rotate(45 53 53)" fill="#4c7fc2"/>
    <path d="M53 38 36 53h5v14h8v-9h8v9h8V53h5z" fill="#fff"/></svg>
</div>
<div class="abs feature feature-body" style="left:352px;top:1488px">
  <h3>In-House Services</h3>
  <p>We have honed our craft through decades of attention to detail, expert knowledge, implementation of best practices and unique creativity. Harborline Crest offers you the full package of in-house residential construction services. From land acquisition assistance, preliminary project analysis and cost budgeting, architectural programming, to construction financing and beyond</p>
</div>

<!-- Experience -->
<div class="abs feature" style="left:624px;top:1488px">
  <svg class="icon" viewBox="0 0 106 106"><rect x="23" y="23" width="60" height="60" transform="rotate(45 53 53)" fill="#4c7fc2"/>
    <path d="M53 38l3.5 7.5 8 .8-6 5.5 1.8 8L53 55.8 45.7 60l1.8-8-6-5.5 8-.8z" fill="#fff"/>
    <path d="M38 52c0 9 6 15 15 15s15-6 15-15" fill="none" stroke="#fff" stroke-width="2.5"/></svg>
</div>
<div class="abs feature feature-body" style="left:757px;top:1488px">
  <h3>Experience</h3>
  <p>At Harborline Crest Builds, Inc. we are synonymous with experience, as a matter of fact, we have built over 300,000 square feet of luxury real-estate, in some of the most prestigious addresses in Miami-Dade County. Our portfolio of custom homes ranges from 6,000 square feet to over 19,000 square feet.</p>
</div>

<section class="abs portfolio">
  <h2 class="abs section-title">PORTFOLIO</h2>
  <div class="abs card" style="left:22px;top:102px">
    <div class="photo p1" role="img" aria-label="Mediterranean estate with tile roof among tall trees"></div>
    <div class="abs caption">Design-Build Grand Plantation</div>
  </div>
  <div class="abs card" style="left:415px;top:102px">
    <div class="photo p2" role="img" aria-label="White villa framed by palm trees under blue sky"></div>
    <div class="abs caption">Design-Build Grand Plantation</div>
  </div>
  <div class="abs card" style="left:22px;top:380px">
    <div class="photo p3" role="img" aria-label="Two-storey stone residence with arched windows and garden"></div>
    <div class="abs caption">Design-Build Grand Plantation</div>
  </div>
  <div class="abs card" style="left:415px;top:380px">
    <div class="photo p4" role="img" aria-label="Gated entry with terracotta facade behind tropical plants"></div>
    <div class="abs caption">Design-Build Grand Plantation</div>
  </div>
</section>

<footer class="abs footer">
  <div class="abs contact" style="left:40px;top:34px;padding-left:45px">
    <svg width="18" height="22" viewBox="0 0 18 22"><path d="M9 0a8 8 0 0 0-8 8c0 6 8 14 8 14s8-8 8-14a8 8 0 0 0-8-8zm0 11a3 3 0 1 1 0-6 3 3 0 0 1 0 6z" fill="#fff"/></svg>
    A: 4820 SW 61ST TERRACE, MIAMI, FL 33155
  </div>
  <div class="abs contact" style="left:40px;top:80px;padding-left:45px">
    <svg width="22" height="22" viewBox="0 0 22 22"><path d="M5 1l4 5-2.5 2.5c1.2 2.8 3.3 4.9 6 6L15 12l5 4-2 4c-9 0-17-8-17-17z" fill="#fff"/></svg>
    T. 305-555-0148<br>F. 305-555-0172
  </div>
  <div class="abs footer-split"></div>
  <div class="abs follow" style="left:498px;top:42px;width:210px">
    <div class="follow-title">Follow Us</div>
    <div class="socials" aria-label="Social links">
      <span></span><span></span><span></span><span></span><span></span>
    </div>
  </div>
</footer>
<div class="abs shadow" style="left:257px;top:2646px;width:694px;height:36px"></div>

<p class="abs unsub"><a href="#">unsubscribe from this list</a></p>

</body>
</html>
```